Brava Set CEO and Partners Business Card

We need a fresh, fun, simple and clean business card design....we would like a template where we can add a name and title (as well as specific email addresses). We are open to different looks (full logo on one side and a small logo on the company info side, or our logo is in the background but faint on one side but full on the other, or something else cool :-) ). Our colors are in our logo: blue, black and white...however we are not opposed to the use of other colors if it works. We build sets, make props and a host of other things for the film and television industry...our card should reflect creativity, style and professionalism.

A white background would be preferred.

I would like to see an option with Facebook and Instagram icons.

Facebook- facebook.com/bravasetny
Instagram- brava_set

Our website is bravaset-example.com.

Brava Set, Inc.
418 Corvell Avenue, Unit 9
North Hollywood, California 91602
555.210.4873 | tel
555.210.6692 | fax
www.BravaSet-example.com

Sample Name and Title #1:

Peter Halvik
CEO / Co-Owner
555.210.4873 | tel
555.210.6692 | fax
peter@bravaset-example.com
www.BravaSet-example.com

Target Market(s)

Marketing Professionals, Production Designers, Interior Designers, Film Producers, Directors, Art Directors, Event Directors

Industry/Entity Type

Entertainment Industry

Contact Information for Business Card

Peter Halvik
CEO / Co-Owner
555.210.4873 | tel
555.210.6692 | fax
peter@bravaset-example.com
www.BravaSet-example.com

Font styles to use
Sans Serif

Colors
33a6d7
ffffff
1b1b1b

Requirements
Must have
• Logo, All Contact Info, White Background. Symmetry.
Nice to have
• Facebook and Instagram icons with addresses
• Facebook- facebook.com/bravasetny
• Instagram- brava_set

```html
<!DOCTYPE html>
<html lang="en">
<head>
<meta charset="utf-8">
<title>Brava Set – Business Card</title>
<link rel="stylesheet" href="https://fonts.googleapis.com/css2?family=Roboto:wght@400;500;900&display=swap">
<style>
  :root {
    --brand-blue: #33a6d7;
    --brand-black: #1b1b1b;
    --card-white: #ffffff;
    --text-grey: #5a5a5a;
    --rule-grey: #cfcfcf;
    --backdrop: #e9e9e9;
  }
  * { margin: 0; padding: 0; box-sizing: border-box; }
  html, body {
    width: 1200px; height: 1000px; overflow: hidden;
    background: var(--backdrop);
    font-family: "Roboto", Arial, sans-serif;
  }
  .canvas { position: relative; width: 1200px; height: 1000px; }
  .card {
    position: absolute; left: 220px; width: 760px; height: 434px;
    background: var(--card-white);
    box-shadow: 0 4px 12px rgba(0,0,0,0.18);
  }
  .card--front { top: 50px; }
  .card--back { top: 524px; }

  .wordmark {
    font-family: "Roboto", Arial, sans-serif;
    font-weight: 900; color: var(--brand-black);
    letter-spacing: -1px; white-space: nowrap; line-height: 1;
  }
  .card--front .wordmark {
    position: absolute; left: 0; right: 0; top: 168px;
    text-align: center; font-size: 104px;
  }
  .front-url {
    position: absolute; left: 0; right: 0; top: 380px;
    text-align: center; font-size: 17px; color: var(--text-grey);
  }

  .card--back .wordmark {
    position: absolute; left: 60px; width: 290px; top: 186px;
    text-align: center; font-size: 56px;
  }
  .divider {
    position: absolute; left: 365px; top: 98px; width: 1px; height: 238px;
    background: var(--rule-grey);
  }
  .contact {
    position: absolute; left: 383px; top: 94px;
    color: var(--text-grey); font-size: 17px; line-height: 22px;
  }
  .contact__name { color: var(--brand-blue); font-size: 22px; font-weight: 500; line-height: 28px; }
  .contact__title { margin-bottom: 14px; }
  .contact__address { margin-bottom: 8px; }
  .contact__list { list-style: none; }
  .contact__list li { display: flex; align-items: center; gap: 6px; }
  .contact__list svg { width: 13px; height: 13px; flex: none; fill: var(--brand-blue); }
</style>
</head>
<body>
<div class="canvas">

  <section class="card card--front">
    <div class="wordmark">Brava Set</div>
    <div class="front-url">www.BravaSet-example.com</div>
  </section>

  <section class="card card--back">
    <div class="wordmark">Brava Set</div>
    <div class="divider"></div>
    <div class="contact">
      <div class="contact__name">Peter Halvik</div>
      <div class="contact__title">CEO / Co-Owner</div>
      <div class="contact__address">418 Corvell Avenue, Unit 9<br>North Hollywood, California 91602</div>
      <ul class="contact__list">
        <li><svg viewBox="0 0 16 16"><path d="M3 1l3 3-1.5 2a9 9 0 0 0 5.5 5.5L12 10l3 3-2 2C7 15 1 9 1 3z"/></svg>555.210.4873</li>
        <li><svg viewBox="0 0 16 16"><rect x="4" y="1" width="8" height="4"/><rect x="1" y="6" width="14" height="6" rx="1"/><rect x="4" y="10" width="8" height="5" fill="#fff" stroke="#33a6d7" stroke-width="1.5"/></svg>555.210.6692</li>
        <li><svg viewBox="0 0 16 16"><rect x="1" y="3" width="14" height="10"/><path d="M1 3l7 6 7-6" fill="none" stroke="#fff" stroke-width="1.3"/></svg>peter@bravaset-example.com</li>
        <li><svg viewBox="0 0 16 16"><circle cx="8" cy="8" r="7"/><path d="M1 8h14M8 1c-3 4-3 10 0 14M8 1c3 4 3 10 0 14" fill="none" stroke="#fff" stroke-width="1"/></svg>www.BravaSet-example.com</li>
        <li><svg viewBox="0 0 16 16"><rect x="2" y="2" width="12" height="12"/></svg>/bravasetny</li>
        <li><svg viewBox="0 0 16 16"><rect x="2" y="2" width="12" height="12"/></svg>brava_set</li>
      </ul>
    </div>
  </section>

</div>
</body>
</html>
```